Quorvix Letter head

Quorvix is a young and energetic software development consultancy. We spend our time working with clients to turn what ever is in their heads in to software.
We are trying to create an image of a high class software boutique who build class leading bespoke solutions.
We need a sharp letter head that looks great on high quality media.
We like bold colours and distinctive design. So show us what you can do.
Industry/Entity Type
Software
Requirements
Must have
- Our company is based in the UK and are requried to have on the paper somewhere the following information:
* Registered company name: Quorvix Ltd
* Registered company number
* VAT registration number
In addition we also want the following:
* An email address
* Telephone number
* Website address
An example of what some pages have in their footer is something like the following:
Quorvix Ltd is registered in England and Wales. Reg. no: 5316274
Registered office: 48 Cobblewick Road, Harlow Essex, CM93TP. Tel: 07712365081
You do not have to use this sentance but please make sure your design incorporates accommodates the requirements for UK based companies

```html
<!DOCTYPE html>
<html lang="en">
<head>
<meta charset="utf-8">
<title>Quorvix Letterhead</title>
<link rel="stylesheet" href="https://fonts.googleapis.com/css2?family=Montserrat:wght@400;500&family=Source+Sans+3:wght@400&display=swap">
<style>
  :root {
    --brand-red: #be1622;
    --paper: #ffffff;
    --ink: #1a1a1a;
    --ink-soft: #4a4a4a;
    --faint-red: #fbecec;
    --faint-grey: #f1f1f1;
    --footer-top: #f4f4f4;
    --footer-bottom: #d9d9d9;
  }
  html, body {
    margin: 0;
    padding: 0;
    overflow: hidden;
    background: var(--paper);
  }
  .letterhead {
    position: relative;
    width: 848px;
    height: 1200px;
    overflow: hidden;
    background: var(--paper);
    font-family: "Source Sans 3", "Myriad Pro", Arial, sans-serif;
    color: var(--ink);
  }
  .brand-mark {
    position: absolute;
    left: 25px;
    top: 40px;
    width: 52px;
    height: 52px;
    background: var(--brand-red);
  }
  .header-band {
    position: absolute;
    left: 177px;
    top: 0;
    width: 671px;
    height: 117px;
    background: var(--brand-red);
  }
  .brand-name {
    position: absolute;
    left: 18px;
    top: 28px;
    margin: 0;
    font-family: "Montserrat", Arial, sans-serif;
    font-weight: 400;
    font-size: 52px;
    line-height: 1;
    color: var(--paper);
  }
  .website {
    position: absolute;
    left: 276px;
    top: 62px;
    font-family: "Montserrat", Arial, sans-serif;
    font-weight: 500;
    font-size: 18px;
    letter-spacing: 8px;
    color: var(--paper);
  }
  .backdrop-name {
    position: absolute;
    margin: 0;
    font-family: "Montserrat", Arial, sans-serif;
    font-weight: 400;
    line-height: 1;
    white-space: nowrap;
    pointer-events: none;
  }
  .backdrop-name--upper {
    left: -20px;
    top: 150px;
    font-size: 300px;
    color: var(--faint-red);
  }
  .backdrop-name--lower {
    left: 185px;
    top: 830px;
    font-size: 260px;
    color: var(--faint-grey);
  }
  .footer {
    position: absolute;
    left: 0;
    top: 1097px;
    width: 848px;
    height: 103px;
    background: linear-gradient(to bottom, var(--footer-top), var(--footer-bottom));
  }
  .company-name {
    position: absolute;
    left: 31px;
    top: 34px;
    font-size: 27px;
    line-height: 1;
  }
  .footer-divider {
    position: absolute;
    left: 216px;
    top: 22px;
    width: 5px;
    height: 60px;
    background: var(--brand-red);
  }
  .registration {
    position: absolute;
    left: 246px;
    top: 14px;
    font-size: 17px;
    line-height: 25px;
  }
  .email {
    position: absolute;
    left: 489px;
    top: 26px;
    font-size: 18px;
    letter-spacing: 5.5px;
    line-height: 1;
  }
  .registered-office {
    position: absolute;
    left: 489px;
    top: 54px;
    font-size: 13px;
    line-height: 17px;
    color: var(--ink-soft);
  }
</style>
</head>
<body>
  <div class="letterhead">
    <p class="backdrop-name backdrop-name--upper" aria-hidden="true">Quorvix</p>
    <p class="backdrop-name backdrop-name--lower" aria-hidden="true">Quorvix</p>

    <div class="brand-mark"></div>
    <header class="header-band">
      <h1 class="brand-name">Quorvix</h1>
      <span class="website">www.quorvix.com</span>
    </header>

    <footer class="footer">
      <span class="company-name">Quorvix Ltd.</span>
      <span class="footer-divider"></span>
      <div class="registration">
        <div>Reg. no: 5316274</div>
        <div>VAT no: GB 204 7391 58</div>
        <div>Tel: 07712365081</div>
      </div>
      <span class="email">info@quorvix.com</span>
      <div class="registered-office">
        <div>Registered in England and Wales. Registered office:</div>
        <div>48 Cobblewick Road, Harlow Essex, CM93TP</div>
      </div>
    </footer>
  </div>
</body>
</html>
```